Need a website setup for our new removalist business.
Our business is called Kettle Brook Removals and would like a website setup.
We don’t have a website, logo or design as of yet. Our truck is blue so something possibly that works and can incorporate the blue.

```html
<!DOCTYPE html>
<html lang="en">
<head>
<meta charset="utf-8">
<title>Kettle Brook Removals</title>
<link href="https://fonts.googleapis.com/css2?family=Montserrat:wght@700;800&family=Roboto:wght@400;500;700&display=swap" rel="stylesheet">
<style>
:root{
  --blue:#4a66a8;
  --blue-dark:#3d5896;
  --ink:#1f1f1f;
  --muted:#666;
  --grey-word:#a9a9a9;
  --panel:#f4f4f4;
  --footer:#2a2a2a;
  --footer-base:#1d1d1d;
  --white:#fff;
}
*{margin:0;padding:0;box-sizing:border-box}
html,body{width:1200px;height:3839px;overflow:hidden}
body{font-family:'Roboto',sans-serif;color:var(--ink);background:var(--white);position:relative}
.abs{position:absolute}
.display{font-family:'Montserrat',sans-serif;font-weight:800;letter-spacing:2px;text-transform:uppercase}
.btn{position:absolute;background:var(--blue);color:#fff;font-weight:700;font-size:15px;display:flex;align-items:center;justify-content:center;text-transform:uppercase}
.eyebrow{color:var(--blue);font-weight:500;font-size:21px;text-transform:uppercase}
.soft{color:var(--grey-word)}

/* header */
.topbar{position:absolute;left:612px;top:0;width:588px;height:42px;background:var(--ink);clip-path:polygon(0 0,100% 0,100% 100%,40px 100%);color:#fff;font-size:14px;display:flex;align-items:center;padding-left:58px;gap:10px}
.topbar svg{width:13px;height:13px;fill:var(--blue)}
.header{position:absolute;left:0;top:0;width:1200px;height:143px;background:#fff}
.brand{position:absolute;left:110px;top:24px;width:190px;height:150px;background:#fff;z-index:3;display:flex;align-items:center;gap:10px;padding-left:4px}
.brand .mark{width:26px;height:26px;background:var(--blue);flex:none}
.brand .name{font-family:'Montserrat',sans-serif;font-weight:800;font-size:17px;line-height:21px;color:var(--blue);text-transform:uppercase}
.nav a{position:absolute;top:84px;font-size:15px;font-weight:500;color:var(--ink);text-decoration:none;text-transform:uppercase}
.nav a.active{color:var(--blue);border-bottom:2px solid var(--blue);padding-bottom:2px}
.quote{left:942px;top:67px;width:146px;height:51px}

/* hero */
.hero{position:absolute;left:0;top:143px;width:1200px;height:697px;background:linear-gradient(180deg,#8ea3bf 0%,#b9a48a 45%,#8a6a45 65%,#3d3a33 100%)}
.hero-copy{position:absolute;left:110px;top:170px;color:#fff}
.hero-copy .kicker{font-size:21px;font-weight:500;text-transform:uppercase}
.hero-copy h1{font-size:44px;margin-top:4px}
.hero-copy .rule{width:92px;height:3px;background:#fff;margin-top:8px}
.hero-copy p{font-size:20px;line-height:30px;margin-top:20px;width:560px}
.hero .btn{left:112px;top:359px;width:153px;height:51px}
.dots{position:absolute;left:1139px;top:255px;display:flex;flex-direction:column;gap:10px}
.dots span{width:15px;height:15px;border:2px solid #fff;border-radius:50%}
.dots span.on{background:#fff}
.hero-edge{position:absolute;left:0;top:640px;width:1200px;height:200px}

/* about */
.about-photo{left:110px;top:866px;width:447px;height:402px;background:linear-gradient(135deg,#d7c2a6,#a78760 60%,#7d6245);box-shadow:0 10px 30px rgba(0,0,0,.12)}
.about-text{left:629px;top:880px;width:470px}
.about-text h2{font-size:40px;margin-top:4px}
.about-text .rule{position:absolute;left:-29px;top:83px;width:56px;height:3px;background:var(--blue)}
.about-text p{font-size:15px;line-height:26px;color:var(--muted);margin-top:24px}
.about-text p + p{margin-top:15px}

/* services */
.services{position:absolute;left:0;top:1397px;width:1200px;height:966px;background:var(--panel)}
.section-head{position:absolute;left:0;width:1200px;text-align:center}
.section-head h2{font-size:40px;margin-top:2px}
.section-head .rule{width:56px;height:3px;background:var(--blue);margin:4px auto 0}
.service{position:absolute;width:311px;height:323px}
.service .photo{width:311px;height:253px}
.service .card{position:absolute;left:21px;top:184px;width:269px;height:139px;background:#fff;padding:22px 23px;box-shadow:0 6px 18px rgba(0,0,0,.06)}
.service h3{font-size:18px;font-weight:500;text-transform:uppercase}
.service p{font-size:13px;line-height:23px;color:var(--muted);margin-top:6px}
.service a{display:block;font-size:12px;font-weight:700;color:var(--blue);margin-top:6px;text-decoration:none;text-transform:uppercase}

/* trust */
.trust-frame{left:827px;top:2478px;width:261px;height:419px;background:#adadad}
.trust-photo{left:595px;top:2516px;width:454px;height:342px;background:linear-gradient(135deg,#e8e4dc,#b9a58d 55%,#7c6a58)}
.trust-text{left:136px;top:2486px;width:404px}
.trust-text h2{font-size:34px;line-height:38px;margin-top:8px}
.trust-text .rule{position:absolute;left:-24px;top:109px;width:44px;height:3px;background:var(--blue)}
.trust-text p{font-size:14.5px;line-height:25.6px;color:#444;text-align:justify;margin-top:40px}
.trust .btn{left:139px;top:2832px;width:146px;height:51px}

/* contact */
.contact{position:absolute;left:0;top:3016px;width:1200px;height:472px;background:linear-gradient(180deg,var(--blue),var(--blue-dark))}
.contact .section-head{top:64px;color:#fff}
.contact .kicker{font-size:19px;font-weight:500;text-transform:uppercase}
.contact h2{font-size:40px;color:#fff}
.contact h2 u{text-decoration:none;border-bottom:3px solid #fff}
.field{position:absolute;background:#fff;border-radius:4px;font-size:14px;color:#555;padding:14px 17px}
.send{position:absolute;left:519px;top:353px;width:162px;height:48px;background:var(--ink);color:#fff;font-size:15px;font-weight:700;display:flex;align-items:center;justify-content:center}

/* footer */
.footer{position:absolute;left:0;top:3488px;width:1200px;height:298px;background:var(--footer);color:#fff}
.footer .brand-foot{position:absolute;left:112px;top:110px;display:flex;align-items:center;gap:12px}
.footer .brand-foot .mark{width:30px;height:30px;background:var(--blue)}
.footer .brand-foot .name{font-family:'Montserrat',sans-serif;font-weight:800;font-size:19px;line-height:24px;text-transform:uppercase;color:#fff}
.footer h4{position:absolute;top:58px;font-size:17px;font-weight:500;text-transform:uppercase}
.flink{position:absolute;font-size:14px;display:flex;align-items:center;gap:14px}
.flink::before{content:"";width:11px;height:11px;border-radius:50%;background:var(--blue)}
.finfo{position:absolute;left:902px;font-size:12px;line-height:22px;width:220px}
.finfo b{font-size:14px;font-weight:500;display:block;text-transform:uppercase}
.ficon{position:absolute;left:866px;width:12px;height:12px;fill:var(--blue)}
.base{position:absolute;left:0;top:3786px;width:1200px;height:53px;background:var(--footer-base);color:#fff;font-size:12px}
.base .copy{position:absolute;left:0;width:1200px;top:19px;text-align:center}
.social{position:absolute;top:13px;width:30px;height:30px;border:1px solid #ccc}
.social.on{background:var(--blue);border-color:var(--blue)}
</style>
</head>
<body>

<header class="header">
  <div class="brand"><span class="mark"></span><span class="name">Kettle Brook<br>Removals</span></div>
  <nav class="nav">
    <a class="active" style="left:412px">Home</a>
    <a style="left:487px">About Us</a>
    <a style="left:591px">Our Services &#9662;</a>
    <a style="left:744px">Blog</a>
    <a style="left:814px">Contact Us</a>
  </nav>
  <div class="btn quote">Get a Quote</div>
</header>
<div class="topbar">
  <svg viewBox="0 0 24 24"><path d="M6.6 10.8a15 15 0 0 0 6.6 6.6l2.2-2.2c.3-.3.7-.4 1-.2 1.1.4 2.3.6 3.6.6.6 0 1 .4 1 1V20c0 .6-.4 1-1 1C10.6 21 3 13.4 3 4c0-.6.4-1 1-1h3.5c.6 0 1 .4 1 1 0 1.3.2 2.5.6 3.6.1.3 0 .7-.2 1z"/></svg>
  <span>+1 (888) 888 8888</span><span style="margin:0 8px">|</span>
  <svg viewBox="0 0 24 24"><path d="M2 5h20v14H2zM2 5l10 8 10-8"/></svg>
  <span>info@kettlebrookremovals.com</span>
</div>

<section class="hero" role="img" aria-label="City skyline with river and bridge at sunset">
  <div class="hero-copy">
    <div class="kicker">Kettle Brook Removals</div>
    <h1 class="display">Moving Made Easy</h1>
    <div class="rule"></div>
    <p>Lorem ipsum dolor sit amet, consectetur adipiscing elit, sed do eiusmod incididunt ut laborea.</p>
  </div>
  <div class="btn">Get Started</div>
  <div class="dots"><span></span><span class="on"></span><span></span><span></span></div>
</section>
<svg class="hero-edge" viewBox="0 0 1200 200" preserveAspectRatio="none">
  <polygon points="290,17 1200,113 1200,190 306,32" fill="#4a66a8"/>
  <polygon points="0,172 306,32 1200,190 1200,200 0,200" fill="#fff"/>
</svg>

<section class="about">
  <div class="abs about-photo" role="img" aria-label="Family unpacking moving boxes at home"></div>
  <div class="abs about-text">
    <div class="eyebrow">About Us</div>
    <h2 class="display">Who <span class="soft">We Are</span></h2>
    <div class="rule"></div>
    <p>Sed ut perspiciatis unde omnis iste natus error sit voluptatem accusantium doloremque laudantium, totam rem aperiam, eaque ipsa quae ab illo inventore veritatis et quasi architecto beatae vitae dicta sunt explicabo.</p>
    <p>Nemo enim ipsam voluptatem quia voluptas sit aspernatur aut odit aut fugit, sed quia consequuntur.</p>
  </div>
  <div class="btn" style="left:629px;top:1198px;width:140px;height:51px">Read More</div>
</section>

<section class="services">
  <div class="section-head" style="top:78px">
    <div class="eyebrow" style="font-size:19px">Our Services</div>
    <h2 class="display">What <span class="soft">We Do</span></h2>
    <div class="rule"></div>
  </div>

  <article class="service" style="left:112px;top:203px">
    <div class="photo" role="img" aria-label="Movers carrying boxes" style="background:linear-gradient(135deg,#e6e2dc,#bfa98c)"></div>
    <div class="card"><h3>Packing Services</h3><p>Excepteur sint occaecat cupidatat non proident, sunt in culpa</p><a>View Details</a></div>
  </article>
  <article class="service" style="left:444px;top:203px">
    <div class="photo" role="img" aria-label="Family moving boxes in sunlit room" style="background:linear-gradient(135deg,#c98f45,#f0c27a 50%,#8c6a48)"></div>
    <div class="card"><h3>Storage Solutions</h3><p>Excepteur sint occaecat cupidatat non proident, sunt in culpa</p><a>View Details</a></div>
  </article>
  <article class="service" style="left:777px;top:203px">
    <div class="photo" role="img" aria-label="Dog sitting among moving boxes" style="background:linear-gradient(135deg,#ecebe8,#cdb391)"></div>
    <div class="card"><h3>Specialty Item Moving</h3><p>Excepteur sint occaecat cupidatat non proident, sunt in culpa</p><a>View Details</a></div>
  </article>
  <article class="service" style="left:277px;top:562px">
    <div class="photo" role="img" aria-label="Stacked boxes in a bright room" style="background:linear-gradient(135deg,#f1efec,#c9a878)"></div>
    <div class="card"><h3>Local Moving</h3><p>Excepteur sint occaecat cupidatat non proident, sunt in culpa</p><a>View Details</a></div>
  </article>
  <article class="service" style="left:610px;top:562px">
    <div class="photo" role="img" aria-label="Movers outside a house with a garden" style="background:linear-gradient(135deg,#9aa38a,#c8b99c 55%,#7d7a6a)"></div>
    <div class="card"><h3>Residential</h3><p>Excepteur sint occaecat cupidatat non proident, sunt in culpa</p><a>View Details</a></div>
  </article>
</section>

<section class="trust">
  <div class="abs trust-frame"></div>
  <div class="abs trust-photo" role="img" aria-label="Family sitting on sofa under a cardboard roof"></div>
  <div class="abs trust-text">
    <div class="eyebrow" style="font-size:19px">Kettle Brook Removals</div>
    <h2 class="display">Safe, Trusted<br><span class="soft">Moving</span></h2>
    <div class="rule"></div>
    <p>Sed ut perspiciatis unde omnis iste natus error sit voluptatem accusantium doloremque laudantium, totam rem aperiam, eaque ipsa quae ab illo inventore veritatis et quasi architecto beatae vitae dicta sunt explicabo. Nemo enim ipsam voluptatem quia voluptas sit aspernatur aut odit aut fugit, sed quia consequuntur magni dolores eos qui ratione voluptatem sequi nesciunt.</p>
  </div>
  <div class="btn">Contact Us</div>
</section>

<section class="contact">
  <div class="section-head">
    <div class="kicker">Contact Us</div>
    <h2 class="display">Get <u>In</u> Touch</h2>
  </div>
  <div class="field" style="left:165px;top:182px;width:282px;height:47px">Full Name</div>
  <div class="field" style="left:458px;top:182px;width:283px;height:47px">Phone</div>
  <div class="field" style="left:751px;top:182px;width:284px;height:47px">Email Address</div>
  <div class="field" style="left:165px;top:243px;width:870px;height:92px">Message</div>
  <div class="send">SEND MESSAGE</div>
</section>

<footer class="footer">
  <div class="brand-foot"><span class="mark"></span><span class="name">Kettle Brook<br>Removals</span></div>
  <h4 style="left:422px">Quick Links</h4>
  <div class="flink" style="left:429px;top:98px">Home</div>
  <div class="flink" style="left:429px;top:134px">About Us</div>
  <div class="flink" style="left:429px;top:170px">Our Services</div>
  <div class="flink" style="left:429px;top:205px">Blog</div>
  <div class="flink" style="left:429px;top:241px">Contact Us</div>
  <div class="flink" style="left:637px;top:98px">Site Map</div>
  <div class="flink" style="left:637px;top:134px">Disclaimer</div>
  <div class="flink" style="left:637px;top:170px">Privacy Policy</div>
  <div class="flink" style="left:637px;top:205px">Terms Of Use</div>

  <h4 style="left:866px">Contact Info</h4>
  <svg class="ficon" style="top:100px" viewBox="0 0 24 24"><path d="M12 2a7 7 0 0 0-7 7c0 5 7 13 7 13s7-8 7-13a7 7 0 0 0-7-7zm0 9.5A2.5 2.5 0 1 1 12 6.5a2.5 2.5 0 0 1 0 5z"/></svg>
  <div class="finfo" style="top:96px"><b>Address:</b>465, Lorum Ipsum Dolore Sed Seat, Australia</div>
  <svg class="ficon" style="top:172px" viewBox="0 0 24 24"><path d="M6.6 10.8a15 15 0 0 0 6.6 6.6l2.2-2.2c.3-.3.7-.4 1-.2 1.1.4 2.3.6 3.6.6.6 0 1 .4 1 1V20c0 .6-.4 1-1 1C10.6 21 3 13.4 3 4c0-.6.4-1 1-1h3.5c.6 0 1 .4 1 1 0 1.3.2 2.5.6 3.6.1.3 0 .7-.2 1z"/></svg>
  <div class="finfo" style="top:170px"><b>Phone:</b>+1 (888) 888 8888</div>
  <svg class="ficon" style="top:222px" viewBox="0 0 24 24"><path d="M2 5h20v14H2z"/></svg>
  <div class="finfo" style="top:222px"><b>Email:</b>info@kettlebrookremovals.com</div>
</footer>
<div class="base">
  <div class="copy">© 2024 KETTLE BROOK REMOVALS &nbsp;|&nbsp; All Rights Reserved</div>
  <span class="social on" style="left:976px"></span>
  <span class="social" style="left:1017px"></span>
  <span class="social" style="left:1057px"></span>
</div>

</body>
</html>
```